Webdesign für Immobilienmanagement
Zielgruppe
Immobilienmanagement Unternehmen / allg. Hausverwaltung , Hausmeisterservice, Grünanlagenpflege, Unterhaltsreinigung, Winterdienst
Zielgruppe: Mieter und Wohnungseigentümer
Aufgabenstellung
Farben: weiß/grün
keine Kopie der alten Seite
nutzerfreundliche Unternehmenswebseite
Logo vorhanden auf alter Webseite

```html
<!DOCTYPE html>
<html lang="de">
<head>
<meta charset="utf-8">
<title>Grünhof Immobilien-Management</title>
<link href="https://fonts.googleapis.com/css2?family=Lato:wght@400;700;900&display=swap" rel="stylesheet">
<style>
:root{
  --dark:#1e3a16;
  --deep:#172a12;
  --green:#5aab32;
  --lime:#a6ff6e;
  --navbar:#182a13;
  --yellow:#f7b81c;
  --ink:#222;
  --muted:#444;
  --light:#f2f2f2;
  --card:#f8f8f8;
}
*{margin:0;padding:0;box-sizing:border-box}
html,body{width:696px;height:1200px;overflow:hidden}
body{font-family:'Lato',sans-serif;color:var(--ink);position:relative;
  background:linear-gradient(180deg,var(--dark) 0%,#3f7a28 25%,#7ccf4e 60%,var(--lime) 80%,var(--lime) 100%)}
.abs{position:absolute}
.brand{left:87px;top:10px;color:#fff}
.brand-name{font-weight:900;font-size:22px;letter-spacing:.5px;display:flex;align-items:center;gap:6px;line-height:1}
.brand-name .sq{width:14px;height:14px;background:var(--lime);display:inline-block}
.brand-sub{font-weight:700;font-size:6.6px;margin-top:5px;letter-spacing:.2px}
.emergency{left:457px;top:13px;width:151px;height:30px;background:linear-gradient(90deg,#fff,#ddd);border-radius:2px;padding:4px 8px;font-size:6px;line-height:1.25;color:#333}
.emergency b{font-weight:900;color:#111;display:block}
.badge{left:558px;top:13px;width:44px;height:37px;background:var(--yellow);clip-path:polygon(0 0,100% 0,100% 85%,50% 100%,0 85%);text-align:center;font-size:6.2px;font-weight:900;color:#222;line-height:1.1;padding-top:6px}
.badge svg{display:block;margin:0 auto 2px}
.nav{left:87px;top:53px;width:522px;height:29px;background:var(--navbar);display:flex;align-items:center;padding-left:11px}
.nav a{color:#fff;text-decoration:none;font-size:6.8px;font-weight:700;height:29px;line-height:29px;padding:0 15.5px}
.nav a.active{background:var(--lime);color:#1a2a10;padding:0 15px}
.hero{left:87px;top:81px;width:522px;height:240px;background:linear-gradient(180deg,#f3f3f3 0%,#e9ecef 40%,#c9cdb6 58%,#7f9a3a 72%,#79a62b 100%)}
.hero h1{position:absolute;top:82px;width:100%;text-align:center;font-size:19px;font-weight:700;line-height:1.17;color:var(--navbar)}
.dots{position:absolute;top:227px;left:0;width:100%;display:flex;justify-content:center;gap:4.5px}
.dots i{width:4.5px;height:4.5px;border-radius:50%;background:#fff}
.dots i:first-child{background:#222}
.services{left:87px;top:321px;width:522px;height:73px;background:var(--light);display:flex;padding:14px 10px 0}
.svc{flex:1 1 auto;display:flex;flex-direction:column;align-items:center;font-size:7px;text-align:center;line-height:1.2;border-right:1px solid #ddd;padding:0 4px;height:48px}
.svc:last-child{border-right:0}
.svc svg{margin-bottom:4px}
.main{left:87px;top:394px;width:522px;height:701px;background:#fff}
.about-img{left:28px;top:27px;width:172px;height:102px;background:linear-gradient(180deg,#dbe5ec 0%,#cfd8dd 35%,#5d7a4a 60%,#3f6b2e 100%);clip-path:polygon(50% 0,100% 32%,100% 100%,0 100%,0 32%)}
.h2{color:var(--green);font-weight:700;font-size:10.5px}
.about-h{left:232px;top:32px}
.about-t{left:232px;top:59px;width:260px;font-size:7.1px;line-height:10.5px;color:var(--muted)}
.about-t p+p{margin-top:10.5px}
.what-h{left:0;top:171px;width:522px;text-align:center}
.card{top:200px;width:148px;height:186px;background:var(--card);border:1px solid #ddd}
.card .ph{height:102px}
.card h3{color:var(--green);font-weight:700;font-size:8.6px;margin:8px 0 0 12px}
.card ul{list-style:none;margin:3px 0 0 12px;font-size:6.9px;line-height:10.5px;color:var(--muted)}
.card li::before{content:"» ";font-size:6px}
.more{position:absolute;left:13px;bottom:-7px;width:43px;height:14px;background:var(--green);color:#fff;font-size:6.8px;font-weight:700;line-height:14px;padding-left:9px;border-radius:1px}
.callback{left:19px;top:410px;width:484px;height:106px;border-radius:3px;overflow:hidden;background:linear-gradient(90deg,#3f8a2a 0%,#2f6a20 55%,#183212 100%);color:#fff;padding:27px 16px 0}
.callback h2{font-size:12.4px;font-weight:700}
.callback p{font-size:6.5px;margin-top:3px}
.form{display:flex;gap:5px;margin-top:6px}
.field{width:108px;height:16px;background:#fff;border-radius:8px;font-size:6.6px;color:#333;line-height:16px;padding-left:11px}
.send{width:74px;height:16px;border-radius:8px;background:var(--yellow);font-size:7.2px;font-weight:700;color:#222;text-align:center;line-height:16px}
.test-h{left:0;top:538px;width:522px;text-align:center;font-size:15px;font-weight:700;color:var(--navbar)}
.quote{top:574px;width:212px;height:69px;background:var(--card);border:1px solid #ddd;font-size:7px;line-height:10.5px;color:var(--muted);padding:11px 12px}
.quote::after{content:"";position:absolute;left:56px;bottom:-11px;width:14px;height:11px;background:var(--card);border-left:1px solid #ddd;clip-path:polygon(0 0,100% 0,0 100%)}
.who{top:662px;font-size:7.4px;font-weight:700;color:#222}
.arrow{top:595px;width:20px;height:20px;border:1px solid #555;border-radius:50%;display:flex;align-items:center;justify-content:center}
.footer{left:87px;top:1095px;width:522px;height:73px;background:var(--navbar);text-align:center;font-size:6.3px;line-height:10.5px;padding-top:15px;color:#fff}
.footer .g{color:var(--green)}
.footer .links{margin-top:5px;color:var(--green)}
</style>
</head>
<body>
<div class="abs brand">
  <div class="brand-name">GRÜNHOF <span class="sq"></span></div>
  <div class="brand-sub">IMMOBILIEN - MANAGEMENT GMBH</div>
</div>
<div class="abs emergency"><b>NOTDIENST</b>24 Std. am Tag und auch an<br>den Wochenenden!</div>
<div class="abs badge">
  <svg width="10" height="9" viewBox="0 0 10 9"><circle cx="6" cy="4.5" r="3.5" fill="none" stroke="#222" stroke-width=".8"/><path d="M6 2.5v2l1.3 1M0 3h2M0 5h2" stroke="#222" stroke-width=".8" fill="none"/></svg>
  24 STD<br>NOTDIENST
</div>

<nav class="abs nav">
  <a class="active">HOME</a><a>UBER UNS</a><a>HAUSVERWALTUNG</a><a>HAUSMEISTER</a><a>DOWNLOADS</a><a>PARTNERLINKS</a><a>KONTAKT</a>
</nav>

<section class="abs hero" role="img" aria-label="Stadtpanorama mit Hochhäusern hinter einer grünen Parkwiese">
  <h1>Ihr zuverlässiger Dienstleister<br>rund um die Immobilie</h1>
  <div class="dots"><i></i><i></i><i></i><i></i><i></i></div>
</section>

<section class="abs services">
  <div class="svc"><svg width="22" height="22" viewBox="0 0 22 22" fill="none" stroke="#222" stroke-width="1"><path d="M6 10l5-5 5 5v5H6z"/><path d="M2 17c3 0 5-2 8-2h5l-1 3H9"/></svg>Allgemeine<br>Hausverwaltung</div>
  <div class="svc"><svg width="22" height="22" viewBox="0 0 22 22" fill="none" stroke="#222" stroke-width="1"><circle cx="11" cy="8" r="4"/><path d="M6 8a5 5 0 0 1 10 0M4 21c0-4 3-6 7-6s7 2 7 6"/></svg>Kaufmännische<br>Betreuung</div>
  <div class="svc"><svg width="22" height="22" viewBox="0 0 22 22" fill="none" stroke="#222" stroke-width="1"><circle cx="9" cy="12" r="6"/><rect x="14" y="2" width="7" height="5" rx="1"/></svg>Technische<br>Betreuung</div>
  <div class="svc"><svg width="22" height="22" viewBox="0 0 22 22" fill="none" stroke="#222" stroke-width="1"><path d="M5 18l-2-8 3-1 2 5V4h2v9l1-9h2l-1 10 2-8h2l-2 12z"/><path d="M17 3l1 2M20 7h-2"/></svg>Hausmeisterservice</div>
  <div class="svc"><svg width="22" height="22" viewBox="0 0 22 22" fill="none" stroke="#222" stroke-width="1"><circle cx="15" cy="4" r="1.5"/><path d="M15 6l-2 7h4M13 13l-2 6M17 13l1 6M2 20h18M4 17l1 2M7 16l1 3"/></svg>Grünanlagenpflege</div>
  <div class="svc"><svg width="22" height="22" viewBox="0 0 22 22" fill="none" stroke="#222" stroke-width="1"><path d="M3 10l7-6 5 4M4 9v11h10V12"/><rect x="6" y="12" width="2" height="2"/><rect x="6" y="16" width="2" height="2"/><path d="M14 12l6-8"/></svg>Unterhaltsreinigung</div>
  <div class="svc"><svg width="22" height="22" viewBox="0 0 22 22" fill="none" stroke="#222" stroke-width="1"><path d="M11 1v20M2 6l18 10M2 16L20 6M9 3l2 2 2-2M9 19l2-2 2 2"/><circle cx="11" cy="11" r="3"/></svg>Winterdienst</div>
</section>

<main class="abs main">
  <div class="abs about-img" role="img" aria-label="Moderne Villa mit Garten in Hausform ausgeschnitten"></div>
  <h2 class="abs h2 about-h">WER WIR SIND</h2>
  <div class="abs about-t">
    <p>Wir sind ein junges, freundliches, gut ausgebildetes Team, das sich mit all seiner Aufmerksamkeit und Kompetenz um Ihre Wünsche in Sachen Immobilien kümmert. Möchten Sie eine Wohnung mieten, suchen Sie einen Hausmeister ... oder einen Verwalter für Ihre Immobilie?</p>
    <p>Schauen Sie sich unser Leistungsangebot an und überzeugen Sie sich selbst von den Vorteilen, die wir Ihnen bieten können.</p>
  </div>

  <h2 class="abs h2 what-h">WAS WIR TUN</h2>
  <article class="abs card" style="left:19px">
    <div class="ph" role="img" aria-label="Gelbes Einfamilienhaus mit Garten" style="background:linear-gradient(180deg,#e8e4d8,#d9b977 50%,#6e8d3c)"></div>
    <h3>Hausverwaltung</h3>
    <ul><li>Allgemeine Verwaltung</li><li>Kaufmännische Betreuung</li><li>Technische Betreuung</li></ul>
    <span class="more">Mehr ...</span>
  </article>
  <article class="abs card" style="left:187px">
    <div class="ph" role="img" aria-label="Zwei Bauarbeiter mit Bauplan vor Hochhäusern" style="background:linear-gradient(180deg,#d8d8d8,#e08a3a 55%,#3f5a8a)"></div>
    <h3>Hausmeister</h3>
    <ul><li>Hausmeisterservice</li><li>Grünanlagenpflege</li><li>Winterdienst</li><li>Unterhaltsreinigung</li></ul>
    <span class="more">Mehr ...</span>
  </article>
  <article class="abs card" style="left:355px">
    <div class="ph" role="img" aria-label="Handwerker repariert Abfluss unter der Spüle" style="background:linear-gradient(180deg,#e6e2dc,#8a7e72 45%,#2d4fa0 75%,#d8d8d8)"></div>
    <h3>Notdienst</h3>
    <ul><li>Schnell &amp; kompetent</li><li>24 Stunden am Tag, 7 Tage die Woche</li></ul>
    <span class="more">Mehr ...</span>
  </article>

  <section class="abs callback">
    <h2>Fordern Sie einen Rückruf an</h2>
    <p>Sie haben eine Frage zu unserem Serviceangebot? Dann füllen Sie einfach folgendes Formular aus und wir melden uns schnellst-möglich bei Ihnen.</p>
    <div class="form">
      <div class="field">Name:</div><div class="field">E-Mail:</div><div class="field">Telefon:</div><div class="send">SENDEN</div>
    </div>
  </section>

  <h2 class="abs test-h">Was unser Kunde sagt</h2>
  <div class="abs arrow" style="left:10px"><svg width="6" height="9" viewBox="0 0 6 9"><path d="M5 1L1 4.5 5 8" fill="none" stroke="#444"/></svg></div>
  <div class="abs quote" style="left:37px">Lorem ipsum dolor sit amet, consectetur adipiscing elit, sed do eiusmod tempor incididunt ut labore et dolore magna aliqua. Quis ipsum suspendisse ultrices gravida. Risus commodo viverra maecenas accumsan lacus vel facilisis.</div>
  <div class="abs quote" style="left:271px">Lorem ipsum dolor sit amet, consectetur adipiscing elit, sed do eiusmod tempor incididunt ut labore et dolore magna aliqua. Quis ipsum suspendisse ultrices gravida. Risus commodo viverra maecenas accumsan lacus vel facilisis.</div>
  <div class="abs arrow" style="left:490px"><svg width="6" height="9" viewBox="0 0 6 9"><path d="M1 1l4 3.5L1 8" fill="none" stroke="#444"/></svg></div>
  <div class="abs who" style="left:51px">- Mara Linden</div>
  <div class="abs who" style="left:286px">- Mara Linden</div>
</main>

<footer class="abs footer">
  <div class="g">Grünhof Immobilien-Management GmbH • Lindenweg 7 • 04100 Musterstadt</div>
  <div>Telephone: 01234/567-0 • Fax: 01234/567-89 • Email: info@gruenhof-immobilien.de</div>
  <div class="links">Impressum &nbsp;|&nbsp; Datenschutz</div>
</footer>
</body>
</html>
```